Local Finance and Insurance Advising Company from Switzerland needs an impressive banner design.

I am looking for an impressive Banner Design, I need this Banner for Facebook, LinkedIn, YouTube & Google.

I am Advising all kind of peoples who are living here in Switzerland. Young, middle age and old people. People who want to go study, people who are planning to create a family, old people who are, or going to retire. Expatriates who want to leave Switzerland to live in another country, expatriates who are coming to Switzerland. Peoples who ant to build their own business up. All kind of financial, insurance and pension planning's.

The Company Name is: Alpine Counsel
Our slogen / heading is: Clear Counsel, no Pitch

The Company logo can be used for the banner, but I would preffer to have the banner without logo, as the logo will be already in a another field on the social networks.

Since the first impression is the most important, this project is really important to me. I am ready to realize further projects with the one who can create the perfect banner who hits the point as described. I am a start-up company, everything is still on beginning and still much has to be done.

Target Market(s)

private clients

Requirements
Must have
• The banner should give the impression of happiness, safeness, health and freedom. Empowering people and creating freedom lifestyles.
Should not have
• I do not want that the banner looks like we are some kind of broker who is just selling some kind of insurances.

```html
<!DOCTYPE html>
<html lang="en">
<head>
<meta charset="UTF-8">
<title>Alpine Counsel – Banner</title>
<link rel="stylesheet" href="https://fonts.googleapis.com/css2?family=Montserrat:wght@600;700;900&display=swap">
<style>
  :root {
    --stage: #ececec;
    --forest: #46602e;
    --forest-dark: #2c3f1f;
    --mist: #c9d3c8;
    --foam: #eef3f2;
    --water: #5f9ea3;
    --water-deep: #2f6f78;
    --panel: #fbf6ee;
    --accent: #e8262b;
    --ink: #2a2a26;
    --ink-soft: #4a4a40;
    --white: #ffffff;
  }
  * { box-sizing: border-box; margin: 0; padding: 0; }
  html, body {
    width: 1200px;
    height: 557px;
    overflow: hidden;
    background: var(--stage);
    font-family: "Montserrat", Arial, sans-serif;
  }
  .banner {
    position: absolute;
    left: 0;
    top: 56px;
    width: 1200px;
    height: 445px;
    overflow: hidden;
  }
  .scene-photo {
    position: absolute;
    inset: 0;
    background:
      linear-gradient(180deg,
        var(--forest-dark) 0%,
        var(--forest) 30%,
        var(--mist) 48%,
        var(--foam) 62%,
        var(--foam) 78%,
        var(--water) 90%,
        var(--water-deep) 100%);
  }
  .headline-panel {
    position: absolute;
    left: 607px;
    top: 148px;
    width: 593px;
    height: 141px;
  }
  .headline-panel svg {
    position: absolute;
    inset: 0;
  }
  .headline {
    position: absolute;
    left: 75px;
    top: 20px;
    font-weight: 900;
    font-size: 50px;
    line-height: 51px;
    letter-spacing: -0.5px;
    text-transform: uppercase;
    background: linear-gradient(180deg, var(--ink-soft), var(--ink));
    -webkit-background-clip: text;
    background-clip: text;
    color: transparent;
  }
  .cta {
    position: absolute;
    left: 383px;
    top: 93px;
    width: 113px;
    height: 19px;
    background: var(--accent);
    color: var(--white);
    font-size: 10px;
    font-weight: 600;
    line-height: 19px;
    text-align: center;
    white-space: nowrap;
  }
  .brand-name {
    position: absolute;
    left: 957px;
    top: 372px;
    color: var(--accent);
    font-weight: 700;
    font-size: 22px;
    letter-spacing: 0.5px;
    white-space: nowrap;
  }
</style>
</head>
<body>
  <section class="banner">
    <div class="scene-photo" role="img" aria-label="Photograph of a broad waterfall with a wooded rock island, forest hillside above and turquoise water below"></div>

    <div class="headline-panel">
      <svg width="593" height="141" viewBox="0 0 593 141" aria-hidden="true">
        <path d="M0 0 Q8 115 72 141 L104 141 Q34 112 24 0 Z" fill="var(--accent)"/>
        <path d="M24 0 Q34 112 104 141 L593 141 L593 0 Z" fill="var(--panel)"/>
      </svg>
      <h1 class="headline">Clear Counsel<br>No Pitch</h1>
      <div class="cta">Get Started Now</div>
    </div>

    <div class="brand-name">Alpine Counsel</div>
  </section>
</body>
</html>
```